Newsletter Design for Travel - Group -Event Agency

We are looking for a standard Newsletter Design which we can use regularly to send out to a number of clients. The idea is to add 1 or more pictures and a promotion or program as well as some possible news. We are a travel agency and want to promote our products in either the travel sector (B2C) or event and group sector (B2B , see our company logo enclosed.

Target Market(s)

We have different target markets, but in the end it's always connected to the travel industry

Industry/Entity Type

Events

Font styles to use
Sans Serif

Colors
3176b5
eaf1f7

Requirements
Must have
• Area to upload picture(s), text field and business data (website, linkedin, facebook, instagram, tel and e-mail contacts. Subscribe/unsubscrive
Nice to have
• optional CTA Buttom, p.e. "make a virutal appointment" or similar
Should not have
• should stay with the colours of our logo / website - grey, a bit blue

```html
<!DOCTYPE html>
<html lang="en">
<head>
<meta charset="utf-8">
<title>Atlantico Journeys Newsletter</title>
<link href="https://fonts.googleapis.com/css2?family=Poppins:wght@300;400;500;600&family=Arimo:wght@400&family=Montserrat:wght@400;600&display=swap" rel="stylesheet">
<style>
:root{
  --brand-blue:#3176b5;
  --brand-tint:#eaf1f7;
  --page-grey:#ebebeb;
  --bar-grey:#cfcdcb;
  --footer-dark:#2b2b2b;
  --bottom-grey:#f0f0f0;
  --ink:#111111;
  --body-grey:#6e6e6e;
  --white:#ffffff;
}
*{margin:0;padding:0;box-sizing:border-box}
html,body{width:1200px;height:5239px;overflow:hidden}
body{background:var(--page-grey);font-family:"Arimo",Arial,sans-serif;position:relative}
.browser-bar{height:92px;background:var(--bar-grey);display:flex;align-items:center;justify-content:center;font-family:"Arimo",Arial,sans-serif;font-size:27px;color:#333}
.column{position:absolute;left:47px;width:1106px;background:var(--white)}
.hero{top:92px;height:966px;background:linear-gradient(180deg,#6cc4f7 0%,#74c6f5 24%,#c9b38a 42%,#2fc0c8 62%,#1ea8b4 78%,#d9b57e 100%)}
.brand{position:absolute;top:80px;left:0;right:0;display:flex;align-items:center;justify-content:center;gap:20px;font-family:"Poppins",sans-serif;font-weight:600;font-size:54px;line-height:1.2;color:#1d1d1d;letter-spacing:2px}
.brand-dot{width:30px;height:30px;border-radius:50%;background:var(--brand-blue)}
.hero-title{position:absolute;top:500px;left:0;right:0;text-align:center;font-family:"Montserrat",sans-serif;font-weight:600;font-size:130px;color:var(--white);letter-spacing:4px;line-height:1}
.hero-sub{position:absolute;top:655px;left:0;right:0;text-align:center;font-family:"Montserrat",sans-serif;font-weight:400;font-size:44px;line-height:1.2;color:var(--white)}
.hero-btn{position:absolute;left:360px;top:781px;width:384px;height:88px;border:3px solid var(--white);display:flex;align-items:center;justify-content:center;font-family:"Poppins",sans-serif;font-weight:500;font-size:29px;color:var(--white);letter-spacing:1px}
.intro{top:1058px;height:386px;text-align:center}
.section-title{font-family:"Poppins",sans-serif;font-weight:500;font-size:37px;color:var(--ink)}
.intro .section-title{margin-top:62px;text-transform:uppercase}
.body-copy{width:950px;margin:22px auto 0;font-size:26.5px;line-height:41px;color:var(--body-grey)}
.destinations{top:1444px;height:659px;display:flex;background:#000}
.destination{width:369px;display:flex;flex-direction:column}
.destination-photo{height:553px}
.photo-coast{background:linear-gradient(180deg,#1a72e0 0%,#5aa7f0 55%,#3b8a6a 72%,#d9c9a4 100%)}
.photo-beach{background:linear-gradient(180deg,#9a7a4e 0%,#c9c4b7 25%,#8fb4ad 45%,#c8a077 62%,#b98c63 100%)}
.photo-lake{background:linear-gradient(180deg,#b6c2cc 0%,#e3e6ea 30%,#3d6d4b 52%,#507f86 75%,#3c6c66 100%)}
.destination-name{flex:1;display:flex;align-items:center;justify-content:center;text-align:center;font-family:"Poppins",sans-serif;font-weight:500;font-size:27px;line-height:33px;color:var(--white)}
.tours{top:2103px;height:553px;text-align:center}
.tours .section-title{margin-top:62px}
.btn-primary{display:flex;align-items:center;justify-content:center;width:480px;height:92px;margin:62px auto 0;background:var(--brand-blue);font-family:"Poppins",sans-serif;font-weight:500;font-size:29px;color:var(--white);letter-spacing:1px}
.cruise{top:2656px;height:777px;background:linear-gradient(180deg,#7595bd 0%,#86a5c8 50%,#b9c7d6 62%,#2b4671 66%,#1a3057 100%)}
.cruise-title{position:absolute;top:98px;left:0;right:0;text-align:center;font-family:"Poppins",sans-serif;font-weight:600;font-size:66px;line-height:89px;color:var(--white)}
.news{top:3433px;height:478px}
.news-item{position:absolute;top:128px;width:520px}
.news-item.left{left:20px}
.news-item.right{left:583px}
.news-heading{font-family:"Poppins",sans-serif;font-weight:500;font-size:27px;line-height:34px;color:var(--ink)}
.news-copy{margin-top:36px;font-family:"Poppins",sans-serif;font-weight:300;font-size:26px;line-height:45px;color:#7a7a7a}
.contact-band{top:3911px;height:336px;background:var(--brand-blue);text-align:center;color:var(--white)}
.contact-icon{position:absolute;left:507px;top:35px}
.contact-label{position:absolute;top:165px;left:0;right:0;font-family:"Poppins",sans-serif;font-weight:500;font-size:31px;line-height:1.2}
.contact-number{position:absolute;top:212px;left:0;right:0;font-family:"Arimo",Arial,sans-serif;font-size:58px;line-height:1.2;letter-spacing:1px}
.footer{position:absolute;top:4304px;left:0;width:1200px;height:665px;background:var(--footer-dark);color:var(--white);font-family:"Poppins",sans-serif}
.footer-title{position:absolute;top:55px;left:0;right:0;text-align:center;font-weight:500;font-size:39px;letter-spacing:1px}
.footer-rule{position:absolute;left:47px;width:1106px;height:2px;background:#555}
.office{position:absolute;top:222px;width:560px}
.office.left{left:73px}
.office.right{left:661px}
.office-name{font-weight:500;font-size:28px}
.office-address{margin-top:22px;font-size:23px;line-height:45px}
.footer-contacts{position:absolute;top:518px;left:0;right:0;text-align:center;font-size:23px;line-height:45px}
.bottom{position:absolute;top:4969px;left:0;width:1200px;height:270px;background:var(--bottom-grey)}
.social{position:absolute;top:64px;left:446px;display:flex;gap:10px}
.social span{width:92px;height:92px;border-radius:50%;background:var(--brand-blue);display:block}
</style>
</head>
<body>
  <div class="browser-bar">View in web browser</div>

  <section class="column hero" role="img" aria-label="Coastal cliffs with turquoise sea under a blue sky">
    <div class="brand"><span class="brand-dot"></span>ATLANTICO JOURNEYS</div>
    <h1 class="hero-title">PORTUGAL</h1>
    <p class="hero-sub">get to know our conuntry</p>
    <div class="hero-btn">ENQUIRE NOW</div>
  </section>

  <section class="column intro">
    <h2 class="section-title">Welcome to Atlantico Journeys</h2>
    <p class="body-copy">Aenean ornare ligula vel ligula pretium, sed condimentum enim faucibus. Proin blandit velit at enim fringilla, et suscipit dolor malesuada. Fusce sed erat ipsum. Integer scelerisque, felis sit amet commodo aliquam, velit orci molestie tortor, ut aliquet ante elit nec ligula.</p>
  </section>

  <section class="column destinations">
    <div class="destination">
      <div class="destination-photo photo-coast" role="img" aria-label="Tropical beach with rocky islet under blue sky"></div>
      <div class="destination-name">Costa Rica de<br>Costa a Costa</div>
    </div>
    <div class="destination">
      <div class="destination-photo photo-beach" role="img" aria-label="Sun lounger under a straw parasol on a sandy beach"></div>
      <div class="destination-name">Praias<br>da Gâmbia</div>
    </div>
    <div class="destination">
      <div class="destination-photo photo-lake" role="img" aria-label="Green volcanic crater lake under clouds"></div>
      <div class="destination-name">São Miguel<br>e Faial</div>
    </div>
  </section>

  <section class="column tours">
    <h2 class="section-title">Customized Tour Made for You</h2>
    <p class="body-copy">Aenean ornare ligula vel ligula pretium, sed condimentum enim faucibus. Proin blandit velit at enim fringilla, et suscipit dolor malesuada. Fusce sed erat ipsum. Integer scelerisque, felis sit amet commodo aliquam, velit orci molestie tortor, ut aliquet ante elit nec ligula.</p>
    <div class="btn-primary">Explore More Tours</div>
  </section>

  <section class="column cruise" role="img" aria-label="White cruise ship sailing on a deep blue sea">
    <h2 class="cruise-title">PLANEAR &amp; RESERVAR<br>O SEU CRUZEIRO</h2>
  </section>

  <section class="column news">
    <article class="news-item left">
      <h3 class="news-heading">Lorem ipsum est di maria<br>nuno valencia es news</h3>
      <p class="news-copy">Fusce tincidunt sem ligula, quis posu<br>ere metus vestibulum id. Integer aliqu<br>am feugiat cursus. Fusce pharetra<br>quis eros ac malesuada.</p>
    </article>
    <article class="news-item right">
      <h3 class="news-heading">Lorem ipsum est di maria<br>nuno valencia es news</h3>
      <p class="news-copy">Fusce pharetra quis eros ac ma<br>lesuada. Etiam consectetur ligula<br>velit, vel aliquet lectus efficitur est di<br>maint news feed.</p>
    </article>
  </section>

  <section class="column contact-band">
    <svg class="contact-icon" width="92" height="92" viewBox="0 0 92 92" aria-hidden="true">
      <circle cx="46" cy="46" r="44" fill="none" stroke="#ffffff" stroke-width="3"/>
      <path d="M34 30c2-2 4-2 5 0l4 7c1 2 0 3-1 4l-2 2c2 5 6 9 11 11l2-2c1-1 2-2 4-1l7 4c2 1 2 3 0 5l-3 3c-3 3-9 1-16-5s-10-13-8-17z" fill="#ffffff"/>
    </svg>
    <p class="contact-label">For Any Queries Call Us</p>
    <p class="contact-number">+351 200 100 200, 201, 202</p>
  </section>

  <footer class="footer">
    <h2 class="footer-title">ATLANTICO JOURNEYS - RNAVT 9921</h2>
    <div class="footer-rule" style="top:166px"></div>
    <div class="office left">
      <p class="office-name">Algarve (Operations Center):</p>
      <p class="office-address">Rua das Gaivotas 12, Shop 3<br>8500-000 Portimão Portugal</p>
    </div>
    <div class="office right">
      <p class="office-name">Lisbon:</p>
      <p class="office-address">Avenida do Rio 45, Piso 2, Bloco B,<br>1600-000 Lisbon Portugal</p>
    </div>
    <div class="footer-rule" style="top:428px"></div>
    <p class="footer-contacts">Phones : +351 200 100 200, 201, 202 &nbsp;|&nbsp; Mobile: +351 900 000 111<br>Email: hello@atlanticojourneys.example &nbsp;|&nbsp; Web: www.atlanticojourneys.example</p>
  </footer>

  <div class="bottom">
    <div class="social">
      <span role="img" aria-label="Social network link"></span>
      <span role="img" aria-label="Social network link"></span>
      <span role="img" aria-label="Social network link"></span>
    </div>
  </div>
</body>
</html>
```